Veloria Energy (Alternative Energy)

We sell solar panels and geothermal heating and cooling applications.
We want to emphasize that we can offer AFFORDABLE solar and thermal heating applications.
Governmental 30% tax rebate if ordered by 2017.
Solar panels from 40 -90% efficient
Units pay for themselves
Can be used with current (existing) water and heating systems
Lower energy consumption
Great Backup Heaters in case of power outage.
100% solar powered units. Self running thermosphyin design
Low maintenance
Can be Self installed
Saves the environment
Zero Emissions
Increases homes resale value
Great for remote locations
Increases Jobs

Target Market(s)

V.E.

Industry/Entity Type

Solar

Logo Text

The future is here

Number of Pages Required

5+ page

Font styles to use
Serif

Colors
f37122
fbee3e
acd036
ffffff
000000

Requirements
Must have
• Emphasize that we can offer affordable solar and thermal heating applications
• Pays for themselves within 1-3 years
• Solar panels from 40 -90% efficient
• 100% sustainable and renewable
• Very little sun light required
Nice to have
• Very professional clean modern web design
• Needs to achieve sales results.
Should not have
• any lingo. or confusion. Must be simple and effective. Needs to achieve sales results.

```html
<!DOCTYPE html>
<html lang="en">
<head>
<meta charset="utf-8">
<title>Veloria Energy</title>
<link rel="stylesheet" href="https://fonts.googleapis.com/css2?family=Open+Sans:wght@400;600;700&family=Roboto+Condensed:wght@400;700&display=swap">
<style>
:root{
  --green:#8cc63f;
  --green-dark:#7ab32e;
  --orange:#f37122;
  --orange-dark:#d85a12;
  --yellow:#fbee3e;
  --white:#ffffff;
  --black:#000000;
  --ink:#333333;
  --muted:#777777;
  --footer:#1c1c1c;
  --footer-line:#333333;
}
*{margin:0;padding:0;box-sizing:border-box}
html,body{width:1200px;height:2204px;overflow:hidden}
body{font-family:"Open Sans",Arial,sans-serif;color:var(--ink);background:var(--white);position:relative}
h1,h2,h3,h4,.nav a,.caption{font-family:"Roboto Condensed","Arial Narrow",sans-serif}

/* header */
.site-header{height:110px;background:var(--green);display:flex;align-items:center;justify-content:space-between;padding:0 70px 0 90px}
.brand{display:flex;align-items:center;gap:12px;color:var(--white);font-family:"Roboto Condensed",sans-serif;font-weight:700;font-size:30px;letter-spacing:.5px}
.brand-mark{width:32px;height:32px;border-radius:50%;background:var(--orange)}
.nav{display:flex;gap:6px}
.nav a{color:var(--white);text-decoration:none;font-size:14px;font-weight:700;padding:12px 18px;letter-spacing:.5px}
.nav a.active{background:var(--orange)}

/* hero */
.hero{position:relative;height:490px;background:linear-gradient(180deg,#5a95d6 0%,#9cc6ee 45%,#dfe9ef 70%,#4a6c8a 100%)}
.hero .caption{position:absolute;left:180px;top:300px;background:rgba(0,0,0,.6);color:var(--white);font-size:38px;padding:14px 30px}
.hero .caption b{font-weight:700}
.hero .arrow{position:absolute;top:225px;width:36px;height:36px;border-radius:50%;background:rgba(255,255,255,.85)}
.hero .arrow.prev{left:14px}.hero .arrow.next{right:14px}
.hero .arrow svg{display:block;margin:10px auto}

/* features */
.features{position:relative;margin:-110px auto 0;width:960px;display:flex;justify-content:space-between}
.feature{width:300px;height:220px;position:relative;box-shadow:0 4px 10px rgba(0,0,0,.3)}
.feature .photo{height:100%}
.feature h3{position:absolute;left:0;right:0;bottom:0;background:rgba(0,0,0,.65);color:var(--white);font-size:17px;padding:10px 16px;text-transform:uppercase}

/* welcome */
.welcome{text-align:center;padding:32px 120px 0;height:245px}
.section-title{font-size:30px;color:#222;text-transform:uppercase;font-weight:400}
.welcome .title-rule{width:60px;height:3px;background:var(--orange);margin:10px auto 12px}
.welcome .lead{font-size:14px;color:#555;margin-bottom:10px}
.welcome p.body{font-size:12.5px;line-height:22px;color:var(--muted)}

/* benefits */
.benefits{height:495px;background:linear-gradient(180deg,var(--orange) 0%,var(--orange-dark) 100%);color:var(--white);padding:40px 140px 0}
.benefits .section-title{color:var(--white);text-align:center}
.benefits .title-rule{width:60px;height:3px;background:var(--yellow);margin:10px auto 16px}
.benefits .intro{font-size:12.5px;line-height:21px;text-align:center;margin-bottom:34px;opacity:.95}
.benefits-body{display:flex;gap:40px}
.benefits-visual{width:260px;height:240px;background:var(--white);padding:12px;flex:none}
.benefits-visual div{width:100%;height:100%;background:linear-gradient(135deg,#5aa0d8,#8cc63f)}
.benefit-list{list-style:none;flex:1;display:grid;grid-template-columns:1fr 1fr;grid-auto-flow:column;grid-template-rows:repeat(7,auto);column-gap:30px;row-gap:14px;font-size:13px}
.benefit-list li{display:flex;align-items:flex-start;gap:10px;line-height:18px}
.benefit-list svg{flex:none;margin-top:2px}

/* projects */
.projects{height:390px;padding:50px 140px 0;text-align:center}
.projects .title-rule{width:60px;height:3px;background:var(--orange);margin:10px auto 26px}
.project-grid{display:flex;justify-content:space-between}
.project{width:214px;background:var(--white);box-shadow:0 2px 8px rgba(0,0,0,.25);text-align:left;position:relative}
.project .photo{height:140px}
.project p{font-size:12px;line-height:17px;color:#555;padding:10px 12px 18px}
.project .corner{position:absolute;right:0;bottom:0;width:0;height:0;border-left:34px solid transparent;border-bottom:34px solid var(--orange)}

/* footer */
.site-footer{height:230px;background:var(--footer);color:#bbb;display:flex;gap:40px;padding:26px 140px 0;font-size:12px}
.site-footer h4{color:var(--white);font-size:16px;text-transform:uppercase;margin-bottom:14px;border-bottom:1px solid var(--footer-line);padding-bottom:8px}
.footer-col{flex:1}
.news-item{display:flex;gap:10px;margin-bottom:14px}
.news-thumb{width:44px;height:38px;background:linear-gradient(135deg,#4d7fb8,#9dc55a);flex:none}
.news-item a{color:var(--white);display:block;text-decoration:none}
.news-item span{color:#888;font-size:11px}
.links{display:grid;grid-template-columns:1fr 1fr;row-gap:8px;list-style:none}
.links li::before{content:"› ";color:var(--orange)}
.contact-line{display:flex;gap:10px;align-items:center;margin-bottom:11px}
.contact-line b{color:var(--white)}
.social{list-style:none}
.social li{display:flex;align-items:center;gap:10px;margin-bottom:9px}
.social li i{width:18px;height:18px;background:var(--orange);display:block}
.copyright{position:absolute;left:0;right:0;bottom:0;height:44px;background:var(--green);color:var(--white);font-size:12px;display:flex;align-items:center;justify-content:center}
</style>
</head>
<body>

<header class="site-header">
  <div class="brand"><span class="brand-mark"></span>VELORIA ENERGY</div>
  <nav class="nav">
    <a class="active" href="#">HOME</a>
    <a href="#">ABOUT US</a>
    <a href="#">SERVICES</a>
    <a href="#">PROJECTS</a>
    <a href="#">CONTACT US</a>
  </nav>
</header>

<section class="hero" role="img" aria-label="Rooftop solar panels under a bright blue sky with clouds">
  <span class="arrow prev"><svg width="16" height="16" viewBox="0 0 16 16"><path d="M10 3 L5 8 L10 13" stroke="#555" stroke-width="2" fill="none"/></svg></span>
  <span class="arrow next"><svg width="16" height="16" viewBox="0 0 16 16"><path d="M6 3 L11 8 L6 13" stroke="#555" stroke-width="2" fill="none"/></svg></span>
  <div class="caption"><b>AFFORDABLE</b> solar and thermal heating applications</div>
</section>

<section class="features">
  <article class="feature">
    <div class="photo" role="img" aria-label="Solar panel array beside city buildings" style="background:linear-gradient(160deg,#6fa7dc,#3b5f86)"></div>
    <h3>Solar Panels</h3>
  </article>
  <article class="feature">
    <div class="photo" role="img" aria-label="Solar panels in a field at sunset" style="background:linear-gradient(180deg,#f6b04a,#c7621d 60%,#3a3a3a)"></div>
    <h3>Geothermal Applications</h3>
  </article>
  <article class="feature">
    <div class="photo" role="img" aria-label="Solar panels on green grass under the sun" style="background:linear-gradient(180deg,#f1d98a,#8db84a 70%,#5d8a2c)"></div>
    <h3>Solar Panels</h3>
  </article>
</section>

<section class="welcome">
  <h2 class="section-title">Welcome to Veloria Energy</h2>
  <div class="title-rule"></div>
  <p class="lead">We make clean power simple, affordable and ready for every home and business today.</p>
  <p class="body">Our solar panels and geothermal systems help families cut monthly bills while protecting the planet. Each unit is built to work with the heating and water systems you already own, so switching is quick and easy. Most customers see the system pay for itself within one to three years. Our panels need very little sunlight, deliver strong output in every season and come with friendly local support from the first call to the final install and long after it.</p>
</section>

<section class="benefits">
  <h2 class="section-title">Benefits of Our Device</h2>
  <div class="title-rule"></div>
  <p class="intro">Every Veloria system is 100% sustainable and renewable. It runs quietly, lowers your energy use and keeps your home warm even when the grid goes down, all at a price that makes sense for your family.</p>
  <div class="benefits-body">
    <div class="benefits-visual"><div role="img" aria-label="Illustration of a house with solar panels and a green recycling symbol"></div></div>
    <ul class="benefit-list">
      <li><svg width="14" height="14" viewBox="0 0 14 14"><path d="M2 7 L6 11 L12 3" stroke="#fbee3e" stroke-width="2.4" fill="none"/></svg>Governmental 30% tax rebate if ordered by 2017</li>
      <li><svg width="14" height="14" viewBox="0 0 14 14"><path d="M2 7 L6 11 L12 3" stroke="#fbee3e" stroke-width="2.4" fill="none"/></svg>Solar panels from 40-90% efficient</li>
      <li><svg width="14" height="14" viewBox="0 0 14 14"><path d="M2 7 L6 11 L12 3" stroke="#fbee3e" stroke-width="2.4" fill="none"/></svg>Units pay for themselves</li>
      <li><svg width="14" height="14" viewBox="0 0 14 14"><path d="M2 7 L6 11 L12 3" stroke="#fbee3e" stroke-width="2.4" fill="none"/></svg>Can be used with current (existing) water and heating systems</li>
      <li><svg width="14" height="14" viewBox="0 0 14 14"><path d="M2 7 L6 11 L12 3" stroke="#fbee3e" stroke-width="2.4" fill="none"/></svg>Lower energy consumption</li>
      <li><svg width="14" height="14" viewBox="0 0 14 14"><path d="M2 7 L6 11 L12 3" stroke="#fbee3e" stroke-width="2.4" fill="none"/></svg>Great backup heaters in case of power outage</li>
      <li><svg width="14" height="14" viewBox="0 0 14 14"><path d="M2 7 L6 11 L12 3" stroke="#fbee3e" stroke-width="2.4" fill="none"/></svg>100% solar powered units. Self running thermosiphon design</li>
      <li><svg width="14" height="14" viewBox="0 0 14 14"><path d="M2 7 L6 11 L12 3" stroke="#fbee3e" stroke-width="2.4" fill="none"/></svg>Low maintenance</li>
      <li><svg width="14" height="14" viewBox="0 0 14 14"><path d="M2 7 L6 11 L12 3" stroke="#fbee3e" stroke-width="2.4" fill="none"/></svg>Can be self installed</li>
      <li><svg width="14" height="14" viewBox="0 0 14 14"><path d="M2 7 L6 11 L12 3" stroke="#fbee3e" stroke-width="2.4" fill="none"/></svg>Saves the environment</li>
      <li><svg width="14" height="14" viewBox="0 0 14 14"><path d="M2 7 L6 11 L12 3" stroke="#fbee3e" stroke-width="2.4" fill="none"/></svg>Zero emissions</li>
      <li><svg width="14" height="14" viewBox="0 0 14 14"><path d="M2 7 L6 11 L12 3" stroke="#fbee3e" stroke-width="2.4" fill="none"/></svg>Increases home resale value</li>
      <li><svg width="14" height="14" viewBox="0 0 14 14"><path d="M2 7 L6 11 L12 3" stroke="#fbee3e" stroke-width="2.4" fill="none"/></svg>Great for remote locations</li>
      <li><svg width="14" height="14" viewBox="0 0 14 14"><path d="M2 7 L6 11 L12 3" stroke="#fbee3e" stroke-width="2.4" fill="none"/></svg>Increases jobs</li>
    </ul>
  </div>
</section>

<section class="projects">
  <h2 class="section-title">Recent Projects</h2>
  <div class="title-rule"></div>
  <div class="project-grid">
    <article class="project">
      <div class="photo" role="img" aria-label="Rooftop solar installation on a family home" style="background:linear-gradient(160deg,#7fb2e0,#3f6f9c)"></div>
      <p>Family home rooftop array cuts power bills in half.</p><span class="corner"></span>
    </article>
    <article class="project">
      <div class="photo" role="img" aria-label="Solar farm under a cloudy sky" style="background:linear-gradient(160deg,#d9e6f0,#6b8fb0)"></div>
      <p>Community solar field now powers two hundred homes.</p><span class="corner"></span>
    </article>
    <article class="project">
      <div class="photo" role="img" aria-label="Solar panels on a field with trees" style="background:linear-gradient(180deg,#9ccbee,#7da64a)"></div>
      <p>Farm heating system runs fully on clean sun power.</p><span class="corner"></span>
    </article>
    <article class="project">
      <div class="photo" role="img" aria-label="Solar panels glowing at sunrise" style="background:linear-gradient(180deg,#f5c16a,#e07a2a 60%,#5b3a22)"></div>
      <p>Remote cabin stays warm all winter without the grid.</p><span class="corner"></span>
    </article>
  </div>
</section>

<footer class="site-footer">
  <div class="footer-col">
    <h4>Latest News</h4>
    <div class="news-item"><div class="news-thumb" role="img" aria-label="News photo of solar panels"></div><div><a href="#">Solar rebate extended for homes</a><span>Jan 12, 2017</span></div></div>
    <div class="news-item"><div class="news-thumb" role="img" aria-label="News photo of a geothermal unit"></div><div><a href="#">New geothermal units now shipping</a><span>Jan 04, 2017</span></div></div>
  </div>
  <div class="footer-col">
    <h4>Quick Links</h4>
    <ul class="links">
      <li>Home</li><li>Services</li>
      <li>About Us</li><li>Projects</li>
      <li>Our Team</li><li>Pricing</li>
      <li>FAQ</li><li>Contact Us</li>
    </ul>
  </div>
  <div class="footer-col">
    <h4>Contact Us</h4>
    <div class="contact-line"><svg width="14" height="14" viewBox="0 0 14 14"><circle cx="7" cy="7" r="6" fill="#f37122"/></svg><b>VELORIA ENERGY</b></div>
    <div class="contact-line"><svg width="14" height="16" viewBox="0 0 14 16"><path d="M7 1a5 5 0 0 1 5 5c0 4-5 9-5 9S2 10 2 6a5 5 0 0 1 5-5z" fill="#f37122"/><circle cx="7" cy="6" r="2" fill="#1c1c1c"/></svg>2140 Brightfield Road, Denver, CO 80204</div>
    <div class="contact-line"><svg width="14" height="14" viewBox="0 0 14 14"><path d="M3 1h3l1 3-2 1a8 8 0 0 0 4 4l1-2 3 1v3c0 1-1 2-2 2A11 11 0 0 1 1 3c0-1 1-2 2-2z" fill="#f37122"/></svg>+1 (555) 014-2290</div>
    <div class="contact-line"><svg width="14" height="12" viewBox="0 0 14 12"><rect x="0.5" y="0.5" width="13" height="11" fill="#f37122"/><path d="M1 1 L7 7 L13 1" stroke="#1c1c1c" fill="none"/></svg>hello@veloriaenergy.com</div>
  </div>
  <div class="footer-col">
    <h4>Connect Us</h4>
    <ul class="social">
      <li><i></i>Our Page</li>
      <li><i></i>Updates</li>
      <li><i></i>Videos</li>
      <li><i></i>Photos</li>
      <li><i></i>Network</li>
    </ul>
  </div>
</footer>
<div class="copyright">Copyright © 2017 Veloria Energy. All Rights Reserved.</div>

</body>
</html>
```